Inspirational Card with Words of Wisdom to Give to Kids

I run basketball camps and give inspirational messages to elementary schools and high schools (www.brightpathcourts.com).

I would like to create a card that has some inspirational thoughts and words of wisdom on it that I can give away...and that students and athletes will keep in their wallet as a reminder of things I've taught them.

I want it to be clean and classy, while not looking too child-like or business-like, as I'd like to be able to give it out to kids, teenagers, and young adults.

The card will be the size of a regular business card and will be double-sided. I would like to use black, orange, gray, and white as the primary colors, with white or gray likely being the background color.
Updates

You're welcome to leave off the title "Lessons to Carry" if desired and just use "The Golden Compass of Growth" on the front of the card.

Thanks.

If you choose to leave off the poem, which you're welcome to do, please make one minor addition to the 5-point creed:

Add the words "God and" to "Honour others in everything you say and do" so it becomes:

"Honour God and others in everything you say and do."

Target Market(s)

Children, Teenagers, and Young Adults

Industry/Entity Type

Business

Requirements
Must have
• All the content, although the poem could be removed if necessary.
Should not have
• Nothing basketball-specific, as I want to be able to give it out to any child or teenager.

```html
<!DOCTYPE html>
<html lang="en">
<head>
<meta charset="utf-8">
<title>Lessons to Carry – Wallet Card</title>
<link href="https://fonts.googleapis.com/css2?family=Source+Code+Pro:wght@400;600;700&display=swap" rel="stylesheet">
<style>
  :root {
    --page: #1c1c1c;
    --card: #111111;
    --card-light: #1a1a1a;
    --orange: #f7871f;
    --grey: #d2d2d2;
    --grey-dark: #555555;
    --white: #f2f2f2;
    --ink: #1a1a1a;
    --mono: "Source Code Pro", monospace;
  }
  * { box-sizing: border-box; margin: 0; padding: 0; }
  html, body { width: 1200px; height: 1200px; overflow: hidden; background: var(--page); }
  body { position: relative; font-family: var(--mono); color: var(--white); }

  .card {
    position: absolute; left: 200px; width: 800px; height: 504px;
    background: var(--card); border-radius: 22px; overflow: hidden;
    box-shadow: 0 18px 40px rgba(0,0,0,0.5);
  }
  .card--back { top: 58px; }
  .card--front { top: 638px; }

  .card-texture {
    position: absolute; inset: 0;
    background: linear-gradient(160deg, var(--card-light) 0%, var(--card) 60%);
  }

  /* Front */
  .front-band-top { position: absolute; top: 0; left: 0; width: 800px; height: 64px; }
  .front-url {
    position: absolute; top: 8px; right: 32px; font-size: 14px; font-weight: 600; color: var(--ink);
  }
  .front-title {
    position: absolute; top: 62px; left: 0; right: 0; text-align: center;
    color: var(--orange); font-weight: 700; font-size: 28px; letter-spacing: 2px;
  }
  .compass { position: absolute; top: 122px; left: 40px; width: 340px; }
  .compass-heading { color: var(--orange); font-weight: 600; font-size: 16px; margin-bottom: 14px; }
  .rule-group { display: flex; margin-bottom: 10px; }
  .rule-label { width: 84px; color: var(--orange); font-weight: 700; font-size: 15px; line-height: 23px; }
  .rule-list { list-style: none; font-size: 15px; line-height: 23px; }
  .rule-list li::before, .poem-lines li::before, .pledge-bullet::before {
    content: "•"; color: var(--orange); margin-right: 8px;
  }
  .poem { position: absolute; top: 122px; left: 400px; width: 370px; font-size: 14px; line-height: 23px; }
  .poem-intro { color: var(--orange); font-weight: 600; margin-bottom: 6px; }
  .poem-lines { list-style: none; padding-left: 12px; }
  .poem-author { text-align: right; font-size: 12px; color: var(--grey); margin-top: 8px; }
  .front-band-bottom {
    position: absolute; bottom: 0; left: 0; right: 0; height: 40px; background: var(--grey);
    display: flex; align-items: center; padding-left: 30px; font-size: 16px; font-weight: 600; color: var(--ink);
  }

  /* Back */
  .creed { position: absolute; top: 60px; left: 36px; width: 470px; font-size: 13px; line-height: 22px; }
  .creed-heading, .pledge-heading { color: var(--orange); font-weight: 700; font-size: 14px; margin-bottom: 8px; }
  .pledge { position: absolute; top: 60px; left: 520px; width: 250px; font-size: 13px; line-height: 21px; }
  .signature { margin-top: 26px; margin-left: 60px; width: 170px; text-align: center; font-size: 10px; color: var(--grey); }
  .signature-line { border-top: 1px solid var(--grey-dark); padding-top: 3px; margin-bottom: 20px; }
  .motto-lead {
    position: absolute; bottom: 62px; right: 36px; color: var(--orange); font-weight: 700; font-size: 16px;
  }
  .virtues {
    position: absolute; bottom: 0; left: 0; right: 0; height: 48px; background: var(--orange);
    display: flex; align-items: center; justify-content: space-around; padding: 0 24px;
    list-style: none; font-size: 16px; font-weight: 600; color: var(--ink);
  }
  .virtues li + li::before { content: "•"; margin-right: 26px; }
</style>
</head>
<body>

<section class="card card--back" aria-label="Card back">
  <div class="card-texture" role="img" aria-label="Faint repeated title pattern across the dark card background"></div>

  <div class="creed">
    <h2 class="creed-heading">A 5-Point Creed:</h2>
    <p>Be intentional to grow and learn new things each day.</p>
    <p>Honour God and others in everything you say and do.</p>
    <p>Act with integrity and uprightness in all matters.</p>
    <p>Prioritize serving and giving to others above yourself.</p>
    <p>Dream, pray, and aspire for the impossible.</p>
  </div>

  <div class="pledge">
    <h2 class="pledge-heading">Golden Compass &amp; 5-Point Creed Pledge:</h2>
    <p class="pledge-bullet">I commit to doing my best to live out the Golden Compass and 5-Point Creed each day.</p>
    <div class="signature">
      <div class="signature-line">Signature</div>
      <div class="signature-line">Date</div>
    </div>
  </div>

  <p class="motto-lead">Live every day with:</p>
  <ul class="virtues">
    <li>Passion</li><li>Wonder</li><li>Playfulness</li><li>Gratitude</li><li>Love</li>
  </ul>
</section>

<section class="card card--front" aria-label="Card front">
  <div class="card-texture" role="img" aria-label="Faint repeated title pattern across the dark card background"></div>

  <svg class="front-band-top" viewBox="0 0 800 64" aria-hidden="true">
    <polygon points="0,0 800,0 800,30 0,30" fill="#d2d2d2"/>
    <polygon points="0,30 130,30 96,56 0,56" fill="#f7871f"/>
    <polygon points="800,30 700,30 716,56 800,56" fill="#f7871f"/>
  </svg>
  <p class="front-url">www.brightpathcourts.com</p>

  <h1 class="front-title">LESSONS TO CARRY</h1>

  <div class="compass">
    <h2 class="compass-heading">The Golden Compass of Growth</h2>
    <div class="rule-group">
      <span class="rule-label">NEVER</span>
      <ul class="rule-list"><li>Lie</li><li>Cheat</li><li>Steal</li></ul>
    </div>
    <div class="rule-group">
      <span class="rule-label">DON'T</span>
      <ul class="rule-list"><li>Blame</li><li>Complain</li><li>Give Up</li></ul>
    </div>
    <div class="rule-group">
      <span class="rule-label">ALWAYS</span>
      <ul class="rule-list"><li>Be Grateful</li><li>Uplift Others</li><li>Do More Than Your Share</li></ul>
    </div>
  </div>

  <div class="poem">
    <p class="poem-intro">Four things a man must learn to do<br>If he would make his life more true:</p>
    <ul class="poem-lines">
      <li>To think without confusion clearly,</li>
      <li>To love his fellow man sincerely,</li>
      <li>To act from honest motives purely,</li>
      <li>To trust in God and Heaven securely.</li>
    </ul>
    <p class="poem-author">Henry Ashford Lane</p>
  </div>

  <p class="front-band-bottom">“Make each day your masterpiece.” ~ Coach Walter Penrose</p>
</section>

</body>
</html>
```